Glow in the Dark Inks Sales Flyer - Targeted to the music industry

We need help!
We need a creative flyer to tell the music industry about our new, colorful glow in the dark inks that look amazing on T-shirts and concert merchandise.

The flyer will go to merchandising managers for bands around the world. The design needs to be hip and contemporary but not offensive. No f-bombs please! Size is 4” x 6” or 3” x 5”, and will be printed on card stock. Design can be both sides if you want. We expect color but black and white with some fluorescent accents could be cool. Surprise us.
Here’s some copy, and we can fill in the contact info when the design is close to final.

Help your fans get lit with branded T-shirts and merchandise that glows in the dark!

Let our new Starwell Inks light up your next show!

Call us now –
Updates

Hello Designers.

Please keep in mind that although the thought of glow-in-the-dark may trigger a glowing, green color in your creative minds, StarWell Inks has a wide variety of colors to bring to offer. So please be sure to show that it's not only green glow we are promoting but we have a wide range of colors that glow (including pink, purple, white that glow blue, blue, green, orange, yellow, etc.)

Thank you!

```html
<!DOCTYPE html>
<html lang="en">
<head>
<meta charset="utf-8">
<title>StarWell Inks – Glow in the Dark Merchandise</title>
<link rel="stylesheet" href="https://fonts.googleapis.com/css2?family=Oswald:wght@500;700&family=Roboto:wght@400;700;900&display=swap">
<style>
  :root {
    --ink-black: #050505;
    --glow-green: #7fc21f;
    --glow-lime: #b8e04a;
    --glow-purple: #7a2c8e;
    --glow-magenta: #c2399e;
    --glow-blue: #3a78d8;
    --glow-white: #e8ecff;
    --band-dark-green: #4f7d2b;
    --band-light-green: #92b82e;
    --band-purple: #7a2a6c;
    --text-white: #ffffff;
    --text-soft: #f2f2ee;
  }
  html, body {
    margin: 0;
    padding: 0;
    width: 800px;
    height: 1200px;
    overflow: hidden;
    background: var(--ink-black);
  }
  .flyer {
    position: relative;
    width: 800px;
    height: 1200px;
    overflow: hidden;
    background:
      radial-gradient(ellipse 300px 260px at 420px 180px, rgba(127,194,31,0.75), rgba(127,194,31,0) 70%),
      radial-gradient(ellipse 260px 200px at 560px 380px, rgba(184,224,74,0.25), rgba(184,224,74,0) 70%),
      radial-gradient(ellipse 500px 300px at 720px 760px, rgba(194,57,158,0.55), rgba(194,57,158,0) 70%),
      radial-gradient(ellipse 400px 260px at 80px 740px, rgba(122,44,142,0.5), rgba(122,44,142,0) 70%),
      var(--ink-black);
    font-family: "Roboto", Arial, sans-serif;
    color: var(--text-white);
  }
  .brand-name {
    position: absolute;
    left: 0;
    top: 40px;
    width: 800px;
    height: 320px;
  }
  .brand-name text {
    font-family: "Oswald", "Arial Narrow", sans-serif;
    font-weight: 700;
    fill: var(--text-soft);
  }
  .pitch {
    position: absolute;
    left: 0;
    top: 360px;
    width: 800px;
    margin: 0;
    text-align: center;
    font-size: 37px;
    line-height: 44px;
    font-weight: 400;
  }
  .pitch-glow {
    display: block;
    margin-top: 16px;
    font-size: 34px;
  }
  .pitch-glow strong {
    font-size: 56px;
    font-weight: 900;
  }
  .band {
    position: absolute;
    display: flex;
    align-items: center;
    justify-content: center;
    font-family: "Oswald", "Arial Narrow", sans-serif;
    font-weight: 700;
    color: var(--text-white);
    white-space: nowrap;
    line-height: 1;
  }
  .band-new {
    left: 54px;
    top: 542px;
    width: 690px;
    height: 82px;
    background: var(--band-dark-green);
    font-size: 66px;
    letter-spacing: 3px;
    transform: rotate(-1deg);
  }
  .band-name {
    left: 120px;
    top: 634px;
    width: 544px;
    height: 76px;
    background: var(--band-light-green);
    font-size: 68px;
    letter-spacing: 5px;
    transform: rotate(-0.6deg);
  }
  .band-show {
    left: 0;
    top: 716px;
    width: 800px;
    height: 86px;
    background: var(--band-purple);
    font-size: 76px;
    letter-spacing: 1px;
    transform: rotate(-1deg);
  }
  .music-art {
    position: absolute;
    left: 0;
    top: 806px;
    width: 800px;
    height: 394px;
    background:
      radial-gradient(ellipse 180px 120px at 340px 110px, rgba(232,236,255,0.75), rgba(232,236,255,0) 75%),
      radial-gradient(ellipse 320px 200px at 300px 150px, rgba(58,120,216,0.7), rgba(58,120,216,0) 75%),
      radial-gradient(ellipse 320px 240px at 640px 150px, rgba(194,57,158,0.6), rgba(194,57,158,0) 75%),
      radial-gradient(ellipse 260px 160px at 130px 320px, rgba(220,220,220,0.55), rgba(220,220,220,0) 75%),
      radial-gradient(ellipse 140px 180px at 720px 300px, rgba(60,60,60,0.9), rgba(60,60,60,0) 80%),
      radial-gradient(ellipse 140px 120px at 480px 330px, rgba(50,50,50,0.9), rgba(50,50,50,0) 80%),
      linear-gradient(180deg, rgba(40,20,70,0.4) 0%, rgba(60,30,90,0.7) 50%, #151515 100%);
  }
</style>
</head>
<body>
<main class="flyer">
  <svg class="brand-name" viewBox="0 0 800 320" aria-label="StarWell Inks">
    <text x="74" y="240" font-size="262" textLength="664" lengthAdjust="spacingAndGlyphs">StarWell</text>
    <text x="740" y="305" font-size="70" text-anchor="end">Inks</text>
  </svg>

  <p class="pitch">
    Help your fans get lit with branded<br>
    T-shirts and merchandise that
    <span class="pitch-glow"><strong>glows</strong> in the dark!</span>
  </p>

  <div class="band band-new">Let our NEW</div>
  <div class="band band-name">STARWELL INKS</div>
  <div class="band band-show">light up your next show!</div>

  <div class="music-art" role="img" aria-label="Illustration of piano keys, swirling music notes and staff lines, a loudspeaker and a stage speaker cabinet bursting with blue, purple and white light"></div>
</main>
</body>
</html>
```